Lucia Verde a furniture, interior design and home decor Brand

I need complete stationary for a new brand, business card, postcard, letter head, shipping envelopes, tissue paper, etc... I would like to use copper foil on some of these items. I have a logo design. I would like to see

Furniture,Interior Design & Home Decor

Interior Design

Colors
606060
7f7f7f

Must have
• My signature style is spanish medeterrenean, my brand colors is charcoal gray with copper. Would love to see a wrought iron panel illustration created, I have attahced a few samples of wrought iron illustration I am attracted to, also an example of packing that has the pattern in foil.
Should not have
• Will not be using the word Design, only Lucia Verde and LV icon

```html
<!DOCTYPE html>
<html lang="en">
<head>
<meta charset="utf-8">
<title>Lucia Verde – Business Card</title>
<link rel="stylesheet" href="https://fonts.googleapis.com/css2?family=Open+Sans:wght@400;600;700&display=swap">
<style>
  :root {
    --backdrop: #3a3b3d;
    --charcoal: #606060;
    --charcoal-deep: #545454;
    --grey-text: #5e5e5e;
    --copper: #c8612c;
    --copper-light: #f0a274;
    --card-white: #ffffff;
  }
  * { margin: 0; padding: 0; box-sizing: border-box; }
  html, body {
    width: 1200px; height: 1000px; overflow: hidden;
    background: var(--backdrop);
    font-family: "Open Sans", Arial, sans-serif;
  }
  .stage { position: relative; width: 1200px; height: 1000px; }

  .card {
    position: absolute; left: 320px; width: 560px; height: 320px;
    border-radius: 2px;
    box-shadow: 0 14px 30px rgba(0,0,0,.35);
    overflow: hidden;
  }
  .card--back { top: 130px; background: linear-gradient(160deg, var(--charcoal), var(--charcoal-deep)); }
  .card--front { top: 530px; background: linear-gradient(170deg, var(--card-white) 55%, #ececec); }

  /* back */
  .back-mark {
    position: absolute; left: 50%; top: 50%; transform: translate(-50%, -50%);
    width: 150px; height: 150px; border-radius: 50%;
    border: 2px solid var(--copper);
    display: flex; align-items: center; justify-content: center;
  }
  .back-mark__name { color: var(--copper); font-size: 21px; font-weight: 400; }

  /* front */
  .copper-tab {
    position: absolute; left: 58px; top: 0; width: 72px; height: 48px;
    background: linear-gradient(90deg, var(--copper-light), var(--copper));
  }
  .brand {
    position: absolute; left: 34px; top: 48px;
    display: flex; align-items: center; gap: 14px;
  }
  .brand__circle {
    width: 72px; height: 72px; border-radius: 50%;
    border: 2px solid var(--copper);
  }
  .brand__name { color: var(--copper); font-size: 28px; font-weight: 400; }

  .contact {
    position: absolute; right: 26px; bottom: 22px;
    text-align: right; color: var(--grey-text);
  }
  .contact__name { color: var(--copper); font-size: 23px; font-weight: 700; letter-spacing: .5px; line-height: 1.1; }
  .contact__title { font-size: 17px; letter-spacing: .5px; margin-bottom: 14px; }
  .contact__line { font-size: 17px; line-height: 1.3; }
  .contact__row { display: flex; justify-content: flex-end; align-items: center; gap: 10px; font-size: 17px; line-height: 1.35; }
  .contact__icon { width: 16px; height: 16px; fill: var(--copper); flex: none; }
</style>
</head>
<body>
<main class="stage">

  <section class="card card--back" aria-label="Business card back">
    <div class="back-mark"><span class="back-mark__name">Lucia Verde</span></div>
  </section>

  <section class="card card--front" aria-label="Business card front">
    <div class="copper-tab"></div>
    <div class="brand">
      <span class="brand__circle"></span>
      <span class="brand__name">Lucia Verde</span>
    </div>

    <div class="contact">
      <p class="contact__name">LUCIA VERDE</p>
      <p class="contact__title">PRESIDENT</p>
      <p class="contact__line">2417 Alder Crest Lane</p>
      <p class="contact__line" style="margin-bottom:4px">Maple Hollow, NY 11940</p>
      <p class="contact__row">555 214 7730
        <svg class="contact__icon" viewBox="0 0 16 16" aria-hidden="true"><path d="M3 2l3 0 1 3-2 1.5c.8 1.8 2.2 3.2 4 4L10.5 8.5l3 1v3c0 .8-.7 1.5-1.5 1.5C6.5 14 2 9.5 2 4c0-1 .5-2 1-2z"/></svg>
      </p>
      <p class="contact__row">555 381 0462
        <svg class="contact__icon" viewBox="0 0 16 16" aria-hidden="true"><path d="M4.5 1h7a1 1 0 0 1 1 1v12a1 1 0 0 1-1 1h-7a1 1 0 0 1-1-1V2a1 1 0 0 1 1-1zm.5 2v9h6V3zm3 10a.8.8 0 1 0 0 1.6A.8.8 0 0 0 8 13z"/></svg>
      </p>
      <p class="contact__row">name@luciaverde-home.com
        <svg class="contact__icon" viewBox="0 0 16 16" aria-hidden="true"><path d="M1 3.5h14v9H1zM1.5 4l6.5 5 6.5-5" stroke="#fff" stroke-width="1"/></svg>
      </p>
      <p class="contact__row">www.luciaverde-home.com
        <svg class="contact__icon" viewBox="0 0 16 16" aria-hidden="true"><circle cx="8" cy="8" r="7"/><path d="M1 8h14M8 1c2.5 2.5 2.5 11.5 0 14M8 1c-2.5 2.5-2.5 11.5 0 14" stroke="#fff" stroke-width="1" fill="none"/></svg>
      </p>
    </div>
  </section>

</main>
</body>
</html>
```